Morden, Creative, Unique, Independent Wine Shop

1. We are a brand new wine shop located in Melbourne Australia, we have our logo already, simply use the logo to design a business card.
2. I have uploaded our logo in two versions, with or without shadow, any of them is acceptable.
3. Make it as creative and unique as possible, no limitation of shape, color combination, geometry pattern, fonts, composing etc.
3. Info on the card:
- Brambleford Wine Cellar (Not very necessary if logo is obviously shown)
- 42 Ferncastle Steet, Hampton, Victoria, Australia 3188
- +61 3 9018 4637
- www.bramblefordwinecellar.com.au
- bramblefordwinecellar@mailvista.com
- Additional icons: Google, Instagram, Facebook, Twitter
4. Once again, forget it is a commercial card, make it special.

```html
<!DOCTYPE html>
<html lang="en">
<head>
<meta charset="utf-8">
<title>Brambleford Wine Cellar – Business Card</title>
<link rel="stylesheet" href="https://fonts.googleapis.com/css2?family=Lato:wght@400;700&display=swap">
<style>
  :root {
    --backdrop: #a9a9a9;
    --card: #ffffff;
    --wine: #8e1c2e;
    --accent: #c2184b;
    --ink: #3a3a3a;
    --rule: #6b6b6b;
    --ghost: #f1f1f1;
  }
  * { box-sizing: border-box; margin: 0; padding: 0; }
  html, body { width: 1200px; height: 900px; overflow: hidden; }
  body {
    background: var(--backdrop);
    font-family: "Lato", Arial, sans-serif;
    position: relative;
  }
  .card {
    position: absolute;
    width: 560px;
    height: 320px;
    background: var(--card);
    border-radius: 18px;
    box-shadow: 0 6px 18px rgba(0,0,0,0.25);
    overflow: hidden;
  }
  .card--front { left: 110px; top: 90px; }
  .card--back  { left: 530px; top: 490px; }

  .brand {
    position: absolute;
    display: flex;
    align-items: center;
    gap: 12px;
  }
  .brand__dot {
    width: 34px; height: 34px;
    border-radius: 50%;
    background: var(--wine);
    flex: none;
  }
  .brand__name {
    color: var(--wine);
    font-weight: 400;
    font-size: 21px;
    letter-spacing: 1.5px;
    line-height: 1.15;
    text-transform: uppercase;
  }
  .card--front .brand { left: 150px; top: 132px; }
  .card--back .brand { left: 42px; top: 178px; }
  .card--back .brand__name { font-size: 18px; }

  .ghost-mark {
    position: absolute;
    right: 40px; top: -30px;
    width: 220px; height: 220px;
    border-radius: 50%;
    background: var(--ghost);
  }
  .front__web {
    position: absolute;
    right: 60px; bottom: 42px;
    font-size: 13px;
    color: var(--ink);
  }

  .divider {
    position: absolute;
    left: 268px; top: 62px;
    width: 1px; height: 150px;
    background: var(--rule);
  }
  .contact {
    position: absolute;
    left: 290px; top: 62px;
    color: var(--ink);
    font-size: 13px;
    line-height: 1.4;
  }
  .contact__title {
    color: var(--accent);
    font-size: 15px;
    text-transform: uppercase;
    letter-spacing: 0.3px;
  }
  .contact__address { margin-bottom: 14px; }
  .contact__line { display: flex; align-items: center; gap: 6px; }
  .contact__line svg { width: 11px; height: 11px; fill: var(--accent); flex: none; }

  .social {
    position: absolute;
    left: 330px; top: 252px;
    display: flex; gap: 8px;
  }
  .social__item {
    width: 22px; height: 22px;
    border-radius: 50%;
    background: var(--accent);
  }
</style>
</head>
<body>

  <section class="card card--front">
    <div class="ghost-mark" aria-hidden="true"></div>
    <div class="brand">
      <span class="brand__dot"></span>
      <span class="brand__name">Brambleford<br>Wine Cellar</span>
    </div>
    <p class="front__web">www.bramblefordwinecellar.com.au</p>
  </section>

  <section class="card card--back">
    <div class="brand">
      <span class="brand__dot"></span>
      <span class="brand__name">Brambleford<br>Wine Cellar</span>
    </div>
    <div class="divider"></div>
    <div class="contact">
      <p class="contact__title">Brambleford Wine Cellar</p>
      <p class="contact__address">42 Ferncastle Steet, Hampton<br>Victoria, Australia 3188</p>
      <p class="contact__line">
        <svg viewBox="0 0 24 24" aria-hidden="true"><path d="M6.6 10.8a15 15 0 0 0 6.6 6.6l2.2-2.2a1 1 0 0 1 1-.25 11.4 11.4 0 0 0 3.6.57 1 1 0 0 1 1 1V20a1 1 0 0 1-1 1A17 17 0 0 1 3 4a1 1 0 0 1 1-1h3.5a1 1 0 0 1 1 1c0 1.25.2 2.45.57 3.57a1 1 0 0 1-.25 1z"/></svg>
        +61 3 9018 4637
      </p>
      <p class="contact__line">
        <svg viewBox="0 0 24 24" aria-hidden="true"><path d="M2 5h20v14H2zM3.5 6.5 12 13l8.5-6.5z"/></svg>
        bramblefordwinecellar@mailvista.com
      </p>
      <p class="contact__line">
        <svg viewBox="0 0 24 24" aria-hidden="true"><path d="M12 2a10 10 0 1 0 0 20 10 10 0 0 0 0-20zm1 2.1c1.3.9 2.3 2.9 2.7 5.4H13zm-2 0v5.4H8.3c.4-2.5 1.4-4.5 2.7-5.4zM4.1 11.5h4.1c0 .4 0 .7.1 1H4.1zm0 1.5zM13 13v5.9c1.3-.9 2.3-2.9 2.7-5.9zm-2 0H8.3c.4 3 1.4 5 2.7 5.9zm6.7-1.5h2.2a8 8 0 0 1 0 1h-2.2z"/></svg>
        www.bramblefordwinecellar.com.au
      </p>
    </div>
    <div class="social" aria-label="Social media links">
      <span class="social__item"></span>
      <span class="social__item"></span>
      <span class="social__item"></span>
      <span class="social__item"></span>
    </div>
  </section>

</body>
</html>
```